Business Card Design

I would like a new business card design for an accounting firm that specializes in resolving clients tax problems. I want the card to give the impression that we are not your typical stodgy accounting firm, but at the same time we will get the job done.
Industry/Entity Type
Business
Contact Information for Business Card
Dorian T Welsby
Certified Public Accountant
38-27 52nd Street
Wrenfield, VT 11287
Tel: (402) 555-0142
Fax: (888) 555-0199
e-mail: dtwthecpa@ledgerpost.com
website: harborfilingreliefexperts.com

```html
<!DOCTYPE html>
<html lang="en">
<head>
<meta charset="utf-8">
<title>Dorian T Welsby — Business Card</title>
<link rel="stylesheet" href="https://fonts.googleapis.com/css2?family=Exo+2:wght@400;500;600&display=swap">
<style>
  :root {
    --page-bg: #ecebe8;
    --card-bg: #ffffff;
    --card-edge: #c9c9c9;
    --ink: #111111;
    --ink-soft: #2a2a2a;
  }
  * { margin: 0; padding: 0; box-sizing: border-box; }
  html, body {
    width: 1200px;
    height: 891px;
    overflow: hidden;
    background: var(--page-bg);
  }
  body {
    display: flex;
    align-items: center;
    justify-content: center;
    font-family: "Exo 2", "Segoe UI", sans-serif;
    color: var(--ink);
  }
  .business-card {
    position: relative;
    width: 840px;
    height: 480px;
    background: var(--card-bg);
    border: 10px solid var(--card-edge);
    box-shadow: 0 10px 30px rgba(0,0,0,0.12);
  }
  .contact-list {
    position: absolute;
    left: 70px;
    top: 70px;
    list-style: none;
    font-size: 20px;
    line-height: 28px;
    font-weight: 500;
  }
  .contact-item {
    display: flex;
    align-items: flex-start;
    gap: 14px;
  }
  .contact-icon {
    width: 20px;
    height: 20px;
    margin-top: 4px;
    flex: none;
  }
  .identity {
    position: absolute;
    right: 120px;
    top: 190px;
  }
  .identity-name {
    font-size: 30px;
    font-weight: 600;
    line-height: 1.1;
  }
  .identity-title {
    font-size: 16px;
    font-weight: 400;
    color: var(--ink-soft);
    margin-top: 4px;
  }
  .website {
    position: absolute;
    left: 130px;
    top: 300px;
    display: flex;
    align-items: center;
    gap: 12px;
    font-size: 21px;
    font-weight: 500;
  }
</style>
</head>
<body>
  <main class="business-card">
    <ul class="contact-list">
      <li class="contact-item">
        <svg class="contact-icon" viewBox="0 0 20 20" aria-hidden="true">
          <path d="M10 1.5a6 6 0 0 0-6 6c0 4.5 6 11 6 11s6-6.5 6-11a6 6 0 0 0-6-6z" fill="none" stroke="currentColor" stroke-width="1.8"/>
          <circle cx="10" cy="7.5" r="2.2" fill="currentColor"/>
        </svg>
        <span>38-27 52nd Street,<br>Wrenfield, VT 11287.</span>
      </li>
      <li class="contact-item">
        <svg class="contact-icon" viewBox="0 0 20 20" aria-hidden="true">
          <path d="M5 2l3 4-2 2c1 2.5 3.5 5 6 6l2-2 4 3-2 3C9 17 3 11 2 4z" fill="currentColor"/>
        </svg>
        <span>(402) 555-0142</span>
      </li>
      <li class="contact-item">
        <svg class="contact-icon" viewBox="0 0 20 20" aria-hidden="true">
          <rect x="5" y="2" width="10" height="5" fill="currentColor"/>
          <rect x="2" y="7" width="16" height="7" rx="1" fill="currentColor"/>
          <rect x="5" y="12" width="10" height="6" fill="#fff" stroke="currentColor" stroke-width="1.6"/>
        </svg>
        <span>(888) 555-0199</span>
      </li>
      <li class="contact-item">
        <svg class="contact-icon" viewBox="0 0 20 20" aria-hidden="true">
          <rect x="1.5" y="4" width="17" height="12" fill="currentColor"/>
          <path d="M1.5 4l8.5 7 8.5-7" fill="none" stroke="#fff" stroke-width="1.5"/>
        </svg>
        <span>dtwthecpa@ledgerpost.com</span>
      </li>
    </ul>

    <div class="identity">
      <p class="identity-name">Dorian T Welsby</p>
      <p class="identity-title">Certified Public Accountant</p>
    </div>

    <p class="website">
      <svg class="contact-icon" viewBox="0 0 20 20" aria-hidden="true">
        <circle cx="10" cy="10" r="8.5" fill="currentColor"/>
        <path d="M1.5 10h17M10 1.5c-3 3-3 14 0 17M10 1.5c3 3 3 14 0 17" fill="none" stroke="#fff" stroke-width="1.2"/>
      </svg>
      <span>harborfilingreliefexperts.com</span>
    </p>
  </main>
</body>
</html>
```